Ombrik Partnering Business Card

Hello everyone. We need a business card design that would match our logo and the theme we're trying to have for Ombrik that you can find on our website and/or Linkedin page

```html
<!DOCTYPE html>
<html lang="en">
<head>
<meta charset="utf-8">
<title>Ombrik Partnering Business Card</title>
<link rel="stylesheet" href="https://fonts.googleapis.com/css2?family=Montserrat:wght@600;700&family=Questrial&display=swap">
<style>
  :root {
    --plum: #321f55;
    --ink: #2b2140;
    --paper: #ffffff;
    --backdrop: #e9e4dd;
  }
  * { margin: 0; padding: 0; box-sizing: border-box; }
  html, body { width: 1200px; height: 1200px; overflow: hidden; }
  body { background: var(--backdrop); position: relative; font-family: "Questrial", sans-serif; }

  .card { position: absolute; top: 240px; width: 412px; height: 720px; overflow: hidden; }
  .card--front { left: 146px; background: var(--paper); }
  .card--back { left: 643px; background: var(--plum); }

  .edge-band { position: absolute; left: 0; width: 412px; height: 10px; }
  .edge-band--top { top: 0; }
  .edge-band--bottom { bottom: 0; }

  .wordmark {
    position: absolute; left: 0; width: 100%; text-align: center;
    font-family: "Montserrat", sans-serif; font-weight: 700;
    line-height: 1; letter-spacing: 0.5px;
  }
  .card--front .wordmark { top: 138px; font-size: 36px; color: var(--plum); }
  .card--back .wordmark { top: 296px; font-size: 40px; color: var(--paper); }

  .holder-name {
    position: absolute; top: 282px; width: 100%; text-align: center;
    font-family: "Montserrat", sans-serif; font-weight: 700; font-size: 24px;
    color: var(--plum); letter-spacing: 0.5px;
  }
  .holder-title {
    position: absolute; top: 312px; width: 100%; text-align: center;
    font-size: 16px; color: var(--ink); letter-spacing: 1.5px;
  }
  .title-rule {
    position: absolute; top: 337px; left: 142px; width: 128px; height: 3px; background: var(--plum);
  }

  .contact-icon { position: absolute; left: 186px; width: 40px; height: 40px; }
  .contact-text {
    position: absolute; width: 100%; text-align: center;
    font-size: 16px; color: var(--ink); letter-spacing: 1.6px;
  }

  .address {
    position: absolute; top: 632px; width: 100%; text-align: center;
    font-size: 16px; line-height: 23px; color: var(--ink); letter-spacing: 1.2px;
  }
  .address-rule { position: absolute; top: 654px; height: 3px; background: var(--plum); }
  .address-rule--left { left: 0; width: 88px; }
  .address-rule--right { right: 0; width: 94px; }

  .vertical-url {
    position: absolute; left: 206px; top: 576px;
    transform: translate(-50%, -50%) rotate(-90deg);
    white-space: nowrap; font-size: 16px; color: var(--paper); letter-spacing: 1.6px;
  }
</style>
</head>
<body>

<section class="card card--front">
  <svg class="edge-band edge-band--top" viewBox="0 0 412 10" preserveAspectRatio="none">
    <polygon points="0,0 412,0 412,10 392,10 380,4 32,4 20,10 0,10" fill="var(--plum)"/>
  </svg>

  <div class="wordmark">Ombrik Partnering</div>

  <h1 class="holder-name">DANIEL HARROW</h1>
  <p class="holder-title">President</p>
  <div class="title-rule"></div>

  <svg class="contact-icon" style="top:365px" viewBox="0 0 40 40" aria-label="Phone">
    <circle cx="20" cy="20" r="18" fill="none" stroke="var(--plum)" stroke-width="2.4"/>
    <path d="M14 12.5c1-1 2-1 2.6 0l1.6 2.6c.5.8.3 1.6-.4 2.1l-1 .7c.8 2 2.4 3.6 4.4 4.4l.7-1c.5-.7 1.3-.9 2.1-.4l2.6 1.6c1 .6 1 1.6 0 2.6l-1.2 1.2c-1.2 1.2-3.4 1-6-.7-2.6-1.7-4.6-3.9-6-6.5-1.3-2.4-1.3-4.4-.1-5.6z" fill="var(--plum)"/>
    <path d="M22 12a6 6 0 0 1 6 6M22 15a3 3 0 0 1 3 3" fill="none" stroke="var(--plum)" stroke-width="1.5" stroke-linecap="round"/>
  </svg>
  <p class="contact-text" style="top:414px">+44 2070558142</p>

  <svg class="contact-icon" style="top:450px" viewBox="0 0 40 40" aria-label="Email">
    <circle cx="20" cy="20" r="18" fill="none" stroke="var(--plum)" stroke-width="2.4"/>
    <path d="M11 17l9-6 9 6v10H11z" fill="var(--plum)"/>
    <path d="M11 17l9 6 9-6" fill="none" stroke="var(--paper)" stroke-width="1.5"/>
  </svg>
  <p class="contact-text" style="top:497px">info@ombrikpartnering.com</p>

  <svg class="contact-icon" style="top:537px" viewBox="0 0 40 40" aria-label="Website">
    <circle cx="20" cy="20" r="18" fill="none" stroke="var(--plum)" stroke-width="2.4"/>
    <circle cx="20" cy="20" r="9" fill="var(--plum)"/>
    <path d="M15 16c2 0 3 1 2.5 3s1 3 2.5 4.5M23 13c-1 2 0 3 2 3.5M21 29c0-2 1.5-3 3-3.5" fill="none" stroke="var(--paper)" stroke-width="1.4" stroke-linecap="round"/>
  </svg>
  <p class="contact-text" style="top:581px">www.ombrikpartnering.com</p>

  <div class="address-rule address-rule--left"></div>
  <div class="address-rule address-rule--right"></div>
  <address class="address" style="font-style:normal">
    The Lantern Court Place<br>Crawley, RH10 2QT, UK
  </address>

  <svg class="edge-band edge-band--bottom" viewBox="0 0 412 10" preserveAspectRatio="none">
    <polygon points="0,0 20,0 32,6 380,6 392,0 412,0 412,10 0,10" fill="var(--plum)"/>
  </svg>
</section>

<section class="card card--back">
  <div class="wordmark">Ombrik Partnering</div>
  <p class="vertical-url">www.ombrikpartnering.com</p>
</section>

</body>
</html>
```